Bright-loop stitchworks Business Card

embroidery printing

Target Market(s)

Businesses and public

Industry/Entity Type

Business

Contact Information for Business Card

Front of card..... Bright-loop stitchworks .... Dorian Felkway..... 868 512-7743.... Email... bright_loopstitchworks@mailvane.net

Back of card..... Bright-loop stitchworks embroidery & artwork

Colors
000000

```html
<!DOCTYPE html>
<html lang="en">
<head>
<meta charset="utf-8">
<title>Bright-loop stitchworks — Business Card</title>
<link rel="stylesheet" href="https://fonts.googleapis.com/css2?family=Open+Sans:wght@400;600;700&display=swap">
<style>
  :root {
    --backdrop: #e9e4df;
    --card-light: #f4f1ef;
    --brand-brown: #7b3f1d;
    --ink: #151515;
    --black: #000000;
    --white: #ffffff;
    --card-shadow: 0 10px 30px rgba(0, 0, 0, 0.18);
  }
  * { box-sizing: border-box; margin: 0; padding: 0; }
  html, body {
    width: 1200px;
    height: 900px;
    overflow: hidden;
    background: var(--backdrop);
    font-family: "Open Sans", Arial, sans-serif;
  }
  .canvas {
    position: relative;
    width: 1200px;
    height: 900px;
  }
  .card {
    position: absolute;
    width: 556px;
    height: 343px;
    display: flex;
    flex-direction: column;
    box-shadow: var(--card-shadow);
    overflow: hidden;
  }
  .card--front { left: 238px; top: 62px; }
  .card--back  { left: 458px; top: 518px; width: 560px; }

  .card__brand-area {
    height: 186px;
    background: var(--card-light);
    display: flex;
    align-items: center;
    justify-content: center;
    gap: 14px;
  }
  .brand-mark {
    width: 22px;
    height: 22px;
    background: var(--brand-brown);
  }
  .brand-name {
    font-weight: 700;
    font-size: 38px;
    letter-spacing: 0.5px;
    color: var(--ink);
  }

  .card__info-band {
    flex: 1;
    background: var(--brand-brown);
    display: flex;
    align-items: center;
    padding: 0 0 0 70px;
    gap: 14px;
    color: var(--white);
  }
  .holder-name {
    font-weight: 600;
    font-size: 20px;
    white-space: nowrap;
  }
  .contact-list {
    list-style: none;
    font-size: 14px;
    line-height: 21px;
  }
  .contact-list li {
    display: flex;
    align-items: center;
    gap: 8px;
    white-space: nowrap;
  }
  .contact-list svg { width: 11px; height: 11px; fill: var(--white); flex: none; }

  .card__tagline-band {
    flex: 1;
    background: var(--black);
    display: flex;
    align-items: flex-end;
    justify-content: center;
    padding-bottom: 32px;
  }
  .tagline {
    color: var(--white);
    font-weight: 700;
    font-size: 20px;
    letter-spacing: 0.2px;
  }
</style>
</head>
<body>
<main class="canvas">

  <section class="card card--front" aria-label="Business card front">
    <div class="card__brand-area">
      <span class="brand-mark" aria-hidden="true"></span>
      <span class="brand-name">Bright-loop stitchworks</span>
    </div>
    <div class="card__info-band">
      <p class="holder-name">Dorian Felkway</p>
      <ul class="contact-list">
        <li>
          <svg viewBox="0 0 24 24" aria-hidden="true"><path d="M6.6 10.8a15.1 15.1 0 0 0 6.6 6.6l2.2-2.2a1 1 0 0 1 1-.25 11.4 11.4 0 0 0 3.6.57 1 1 0 0 1 1 1V20a1 1 0 0 1-1 1A17 17 0 0 1 3 4a1 1 0 0 1 1-1h3.5a1 1 0 0 1 1 1c0 1.25.2 2.45.57 3.57a1 1 0 0 1-.25 1z"/></svg>
          868 512-7743
        </li>
        <li>
          <svg viewBox="0 0 24 24" aria-hidden="true"><path d="M2 5h20v14H2z M2 5l10 8 10-8" fill="#fff" stroke="#7b3f1d" stroke-width="2"/></svg>
          bright_loopstitchworks@mailvane.net
        </li>
      </ul>
    </div>
  </section>

  <section class="card card--back" aria-label="Business card back">
    <div class="card__brand-area">
      <span class="brand-mark" aria-hidden="true"></span>
      <span class="brand-name">Bright-loop stitchworks</span>
    </div>
    <div class="card__tagline-band">
      <p class="tagline">EMBROIDERY &amp; ARTWORK</p>
    </div>
  </section>

</main>
</body>
</html>
```